Calvorina Beer Label

I need a label for my beer which is called Calvorina (Latin). The ideia is to have an image of an alchemist in his place of work (something like a laboratory), creating magical potions with the beer ingredients (hops and malts). I will need in the right side of the bottom a small space to write down two informations: ABV and IBU. The size of the label must be 97mm high and 79mm width and we must limit it to 4 colors only.
I added a picture of the model of the beer bottle I will be using, just for reference.
Update:
In addition, Calvorina gives the ideia of something special, occult sciences, especially alchemy; magical, and also something completely sealed (well locked). There is also space to not having the alchemist person itself, as long as we respect this ideia.
We need to link beer, something magical, sealed, etc..
Thanks!

```html
<!DOCTYPE html>
<html lang="en">
<head>
<meta charset="utf-8">
<title>Calvorina Beer Label</title>
<link rel="stylesheet" href="https://fonts.googleapis.com/css2?family=Federo&family=Marcellus&family=Playfair+Display:ital,wght@1,400;1,700&family=Open+Sans:wght@600&display=swap">
<style>
  :root {
    --paper: #ffffff;
    --ink: #231f20;
    --title: #343233;
    --gold: #8f6424;
    --cream: #f3e4d9;
    --ring: #a9a6a8;
    --placeholder-dark: #3a3536;
    --placeholder-light: #6b6264;
    --light: #ffffff;
  }
  html, body {
    margin: 0;
    padding: 0;
    width: 978px;
    height: 1200px;
    overflow: hidden;
    background: var(--paper);
  }
  .label {
    display: block;
    width: 978px;
    height: 1200px;
  }
  .label__base { fill: var(--ink); }
  .label__ring { fill: var(--ring); stroke: var(--ink); stroke-width: 3; }
  .label__field { fill: var(--cream); stroke: var(--ink); stroke-width: 2; }
  .label__inner-line { fill: none; stroke: var(--ink); stroke-width: 4; }
  .label__title-band { fill: var(--cream); }
  .arc-text {
    font-family: "Federo", sans-serif;
    font-size: 84px;
    fill: var(--gold);
  }
  .arc-text--top { letter-spacing: 7px; }
  .arc-text--bottom { letter-spacing: 17px; }
  .brand-name {
    font-family: "Marcellus", serif;
    font-size: 168px;
  }
  .brand-name--shadow { fill: var(--gold); }
  .brand-name--main { fill: var(--title); }
  .variant {
    font-family: "Playfair Display", serif;
    font-style: italic;
    font-weight: 700;
    font-size: 60px;
    fill: var(--gold);
  }
  .art-placeholder { fill: url(#art-tone); }
  .volume {
    font-family: "Playfair Display", serif;
    font-style: italic;
    font-weight: 700;
    font-size: 40px;
    fill: var(--light);
  }
  .spec {
    font-family: "Open Sans", sans-serif;
    font-weight: 600;
    font-size: 30px;
    fill: var(--light);
  }
</style>
</head>
<body>
<svg class="label" viewBox="0 0 978 1200" xmlns="http://www.w3.org/2000/svg">
  <defs>
    <path id="arc-top" d="M 102 640 A 387 482 0 0 1 876 640"/>
    <path id="arc-bottom" d="M 80 600 A 409 506 0 0 0 898 600"/>
    <linearGradient id="art-tone" x1="0" y1="0" x2="0" y2="1">
      <stop offset="0" stop-color="var(--placeholder-dark)"/>
      <stop offset="1" stop-color="var(--placeholder-light)"/>
    </linearGradient>
  </defs>

  <rect class="label__base" x="0" y="585" width="978" height="615"/>

  <ellipse class="label__ring" cx="489" cy="600" rx="486" ry="597"/>
  <ellipse class="label__field" cx="489" cy="600" rx="473" ry="584"/>
  <ellipse class="label__inner-line" cx="489" cy="606" rx="322" ry="408"/>
  <rect class="label__title-band" x="150" y="492" width="678" height="230"/>

  <text class="arc-text arc-text--top" text-anchor="middle">
    <textPath href="#arc-top" startOffset="50%">MAGICALLY BREWED</textPath>
  </text>
  <text class="arc-text arc-text--bottom" text-anchor="middle">
    <textPath href="#arc-bottom" startOffset="50%">PREMIUM QUALITY</textPath>
  </text>

  <rect class="art-placeholder" role="img" aria-label="Illustration of three hop cones, a large one in the centre flanked by two small ones"
        x="350" y="280" width="267" height="203" rx="24"/>

  <text class="brand-name brand-name--shadow" x="503" y="660" text-anchor="middle" textLength="866" lengthAdjust="spacingAndGlyphs">CALVORINA</text>
  <text class="brand-name brand-name--main" x="499" y="656" text-anchor="middle" textLength="866" lengthAdjust="spacingAndGlyphs">CALVORINA</text>

  <text class="variant" x="493" y="714" text-anchor="middle" textLength="266" lengthAdjust="spacingAndGlyphs">Original</text>

  <rect class="art-placeholder" role="img" aria-label="Baroque acanthus scroll ornament with a fleur-de-lis crest"
        x="284" y="747" width="416" height="235" rx="24"/>

  <text class="volume" x="162" y="1146">ml</text>
  <text class="spec" x="810" y="1087">ABV</text>
  <text class="spec" x="810" y="1160">IBU</text>
</svg>
</body>
</html>
```